WordPress design project for Verlani Construction

Verlani Construction, Inc. (www.verlaniinc.example) is a private organization. It is run by the same family that founded Verlani Refuse Systems (www.verlani.example), a large, publicly-held waste management organization in the US. While owned by the same family, the two organizations are run independently.
Verlani Construction is a well-established New England USA construction outfit specializing in site development, heavy excavation, aggregate, large-scale/municipal water and sewer systems, and landfill construction and closure. Verlani Construction is not in any way a residential or commercial building contractor.
Verlani Construction also operates hydraulic and hydrostatic service shops, as well as aggregate (gravel, sand, stone, top soil, and anything else aggregate) sites. Both are for more traditional, non-project customers, such as landscapers and other construction companies.
Business contact information is as noted below:
Address:
Verlani Construction, Inc.
48 Quarry Ridge Road
Mendon, Vermont 05829
Telephone:
802-555-0147
Fax:
802-555-0183
Email:
info@verlaniinc.example
A tagline used in a recent advertisement was:
"Committed to providing a complete array of services for over 30 years, we are New England's premier construction company."
In reviewing design ideas internally, we found bits and pieces of the following sites appealing:
RT Construction (Dorwenski) - http://www.rtconstruction.example/
Halbrook Construction - http://www.halbrook.example/
Pelham Construction - http://www.pelhamconstruction.example/
Riverbend Construction Group - http://www.riverbendconstructiongroup.example/
Krage Construction - http://www.krage.example/
Vail Sisters Construction http://www.vailsis.example/
Tolliver Construction http://www.tolliver-corp.example/
The blue in the logo is hex #00253f. The logo was designed by hand many years ago, so the font is unknown.
We would like a fresh, professional design that effectively illustrates what we do in a thoughtful, impressive way.
Target Market(s)
Would-be clients, land developers, waste organizations, energy developers, engineers, surveyors, landscapers, heavy equipment operators and the likes.
Industry/Entity Type
Waste Management
Requirements
Must have
- Lots of media capabilities, such as embedded video (via YouTube is fine), project image gallery, and sliders for various functions.
A large slider on the landing page is critical, as well as space for standard things, such as news/events, job opportunities, project highlights, and the likes.
We also want to highlight things like employee longevity. Some of our team have been with us since the beginning.
We need to add emphasis to the fact that our hydraulic/hydro static services and aggregate operations are for anyone who needs such service or material. Related, we need a place to set prices and descriptions of such material to help site visitors decide what they may need.
We need a place to highlight business partners, such as Amos Fairley and Gruntwell.
We also need form capabilities for things like bid requests and general contacts from the public. Related, there should be social media capabilities.
Nice to have
- This is almost a must have, but we're open to options. The WordPress design should be capable of fitting into the very popular PlumPages Easel theme.

```html
<!DOCTYPE html>
<html lang="en">
<head>
<meta charset="utf-8">
<title>Verlani Construction</title>
<link href="https://fonts.googleapis.com/css2?family=Mulish:wght@400;600;700&family=Open+Sans:wght@400;600&display=swap" rel="stylesheet">
<style>
:root{
  --navy:#00253f;
  --navy-mid:#0b3a74;
  --page:#f2f2f2;
  --card:#ffffff;
  --line:#dcdcdc;
  --text:#333333;
  --muted:#9a9a9a;
  --link:#1c3f7a;
  --orange:#ee7d22;
  --amber:#f6a632;
}
*{box-sizing:border-box;margin:0;padding:0}
html,body{width:754px;height:1200px;overflow:hidden}
body{position:relative;background:var(--page);font-family:"Mulish",Arial,sans-serif;color:var(--text)}
.abs{position:absolute}
.topbar{left:0;top:0;width:754px;height:3px;background:var(--navy)}
.brand{left:64px;top:22px;width:128px;height:34px;display:flex;align-items:center;gap:6px;color:var(--navy);font-weight:700;font-size:22px;letter-spacing:-.3px}
.brand-mark{width:12px;height:12px;background:var(--navy)}
.nav{left:323px;top:31px;display:flex;font-size:9px;align-items:center}
.nav a{color:var(--navy);text-decoration:none;padding:3px 0;margin-right:19px}
.nav a.active{background:var(--navy);color:#fff;font-weight:700;padding:4px 6px;margin-right:14px}
.nav a:last-child{margin-right:0}
.rule{left:61px;width:618px;height:1px;background:var(--line)}
.tagline{left:61px;top:97px;width:618px;text-align:center;color:var(--navy);font-size:12px;line-height:15px}
.slider{left:61px;top:146px;width:618px;height:249px;overflow:hidden;box-shadow:0 6px 8px -6px rgba(0,0,0,.35);
  background:
    linear-gradient(90deg,rgba(40,45,50,.35) 0%,rgba(40,45,50,.1) 40%,rgba(0,0,0,0) 55%),
    radial-gradient(ellipse 30% 55% at 82% 75%,var(--amber) 0%,rgba(246,166,50,0) 100%),
    radial-gradient(ellipse 28% 60% at 68% 60%,var(--orange) 0%,rgba(238,125,34,0) 100%),
    radial-gradient(ellipse 18% 22% at 70% 18%,#ffffff 0%,rgba(255,255,255,0) 100%),
    linear-gradient(180deg,#a9a395 0%,#c8c0b0 45%,#9d8f7a 100%)}
.slide-title{left:18px;top:80px;color:#fff;font-family:"Open Sans",Arial,sans-serif;font-size:40px;font-weight:600;letter-spacing:-1px;line-height:42px;text-shadow:0 1px 3px rgba(0,0,0,.35)}
.slide-sub{left:22px;top:124px;color:#fff;font-family:"Open Sans",Arial,sans-serif;font-size:28px;line-height:30px;text-shadow:0 1px 3px rgba(0,0,0,.35)}
.btn-light{left:25px;top:166px;background:#fff;color:var(--navy);font-size:8.5px;padding:5px 8px;border-radius:2px;box-shadow:0 1px 2px rgba(0,0,0,.3)}
.dots{left:14px;top:236px;display:flex;gap:2px}
.dots i{width:4px;height:4px;border-radius:50%;background:#c7c7c7}
.dots i:first-child{background:#1b2a44}
.section-bar{left:60px;top:418px;width:619px;height:27px;border-radius:3px;background:linear-gradient(#0e4587,var(--navy));color:#fff;font-size:12px;padding:7px 0 0 13px}
.arrows{right:12px;top:6px;width:38px;height:15px;border-radius:8px;background:#fff;display:flex;justify-content:center;gap:6px;align-items:center}
.card{top:458px;width:127px;height:174px;background:var(--card);box-shadow:0 2px 3px rgba(0,0,0,.12);text-align:center}
.card .pic{height:73px}
.card h3{font-size:9.5px;font-weight:600;margin:12px 0 8px;letter-spacing:.2px}
.card p{font-size:7.2px;line-height:10px;color:var(--muted);padding:0 8px;text-align:left;height:40px;overflow:hidden}
.card a{display:inline-block;margin-top:6px;font-size:7.5px;color:var(--text);text-decoration:underline}
.panel{background:var(--card);border:1px solid #e4e4e4}
.panel-title{height:25px;border-bottom:1px solid #e6e6e6;font-size:10.5px;padding:6px 0 0 7px;background:#fff}
.field{margin:0 0 6px 11px;width:153px;height:17px;border:1px solid #d6d6d6;font-size:6px;color:#888;padding:5px 7px}
.chev{width:14px;height:8px}
.btn-navy{height:20px;background:linear-gradient(#16468c,var(--navy));color:#fff;font-size:9.5px;text-align:center;line-height:20px;border-radius:2px}
.clients{display:grid;grid-template-columns:1fr 1fr;column-gap:6px;padding:6px 8px 0 8px}
.client{font-weight:700;color:var(--navy);font-size:10px;display:flex;align-items:center;justify-content:center;gap:4px;height:42px;white-space:nowrap}
.client span.sq{width:7px;height:7px;background:var(--navy);flex:none}
.work-item{display:flex;gap:8px;margin:13px 0 0 8px}
.work-item .pic{width:81px;height:49px;flex:none}
.work-item b{font-size:7.8px;display:block;margin-bottom:3px}
.work-item p{font-size:6.8px;line-height:10.5px}
.team-pic{width:67px;height:61px;border:1px solid #ccc}
.news p{font-size:6.9px;line-height:12px;color:#888}
.news em{color:var(--link)}
.news .more{text-align:right;font-style:italic;color:#333;font-size:6.9px;margin-top:4px}
.social{left:60px;top:1114px;width:619px;height:34px;background:#fff;box-shadow:0 1px 2px rgba(0,0,0,.12);display:flex;align-items:center}
.social .s{flex:1;display:flex;align-items:center;gap:6px;padding-left:18px;border-right:1px solid #e5e5e5;height:20px}
.social .s:last-child{border-right:none}
.social small{display:block;font-size:6px;color:var(--muted);line-height:7px}
.social b{display:block;font-size:8.5px;font-weight:600;letter-spacing:.4px;line-height:11px}
.social .ico{width:14px;height:14px;border-radius:2px;flex:none}
.footer{left:0;top:1169px;width:754px;height:31px;background:var(--navy);color:#d5dbe5;font-size:6.8px;text-align:center;line-height:31px}
</style>
</head>
<body>
<div class="abs topbar"></div>

<div class="abs brand"><span class="brand-mark"></span>Verlani</div>
<nav class="abs nav">
  <a class="active">HOME</a><a>Who We Are</a><a>What We do</a><a>Where We Are</a><a>News</a><a>About Us</a>
</nav>
<div class="abs rule" style="top:71px"></div>

<p class="abs tagline">"Committed to providing a complete array of services for over 30 years, we are New England's premier construction company."</p>

<section class="abs slider" role="img" aria-label="Smiling construction workers in hard hats and orange safety vests in front of a building site">
  <div class="abs slide-title">Technology</div>
  <div class="abs slide-sub">working for you</div>
  <div class="abs btn-light">Read More</div>
  <div class="abs dots"><i></i><i></i><i></i><i></i><i></i></div>
</section>

<div class="abs section-bar">Our Services
  <div class="abs arrows">
    <svg width="5" height="6"><path d="M5 0L0 3L5 6Z" fill="#00253f"/></svg>
    <svg width="5" height="6"><path d="M0 0L5 3L0 6Z" fill="#00253f"/></svg>
  </div>
</div>

<article class="abs card" style="left:74px">
  <div class="pic" role="img" aria-label="Yellow wheel loader" style="background:linear-gradient(#9fb0bf,#d4ad35 55%,#5e5a48)"></div>
  <h3>HEAVY EXCAVATION</h3>
  <p>Lorem Ipsum is simply dummy text of the printing and typesetting industry. Lorem Ipsum has been the industry's</p>
  <a>Read More</a>
</article>
<article class="abs card" style="left:226px">
  <div class="pic" role="img" aria-label="Worker beside a large concrete sewer pipe" style="background:radial-gradient(circle at 55% 50%,#4a3a30 0 18%,#b9aba0 30%,#8d6e5c 80%)"></div>
  <h3>SEWER SYSTEMS</h3>
  <p>Lorem Ipsum is simply dummy text of the printing and typesetting industry. Lorem Ipsum has been the industry's</p>
  <a>Read More</a>
</article>
<article class="abs card" style="left:377px">
  <div class="pic" role="img" aria-label="Stacked black and steel pipes" style="background:linear-gradient(135deg,#2a2a2a,#8a8f94 50%,#d0d4d8)"></div>
  <h3>WASTE SYSTEM</h3>
  <p>Lorem Ipsum is simply dummy text of the printing and typesetting industry. Lorem Ipsum has been the industry's</p>
  <a>Read More</a>
</article>
<article class="abs card" style="left:530px">
  <div class="pic" role="img" aria-label="Pile of gravel aggregate" style="background:linear-gradient(#c4baa9,#9c8d7a)"></div>
  <h3>AGGREGATE</h3>
  <p>Lorem Ipsum is simply dummy text of the printing and typesetting industry. Lorem Ipsum has been the industry's</p>
  <a>Read More</a>
</article>

<div class="abs rule" style="top:663px"></div>

<section class="abs panel" style="left:60px;top:700px;width:184px;height:165px">
  <div class="panel-title">Contact Form</div>
  <div style="height:10px"></div>
  <div class="field">Enter your name...</div>
  <div class="field">Enter your email...</div>
  <div class="field" style="height:73px">Enter your comment...</div>
</section>
<section class="abs panel" style="left:273px;top:700px;width:184px;height:165px">
  <div class="panel-title">Our Clients</div>
  <div class="clients">
    <div class="client" style="font-size:9px"><span class="sq"></span>Amos Fairley</div>
    <div class="client" style="font-size:11px">Gruntwell</div>
    <div class="client" style="font-size:14px">Marlow</div>
    <div class="client" style="font-size:14px">Hartwick</div>
    <div class="client" style="font-size:8.5px">Corvane</div>
    <div class="client" style="font-size:8.5px">Beaconridge</div>
  </div>
</section>
<section class="abs panel" style="left:480px;top:700px;width:189px;height:165px">
  <div class="panel-title">Featured Video</div>
  <div role="img" aria-label="Video still of hands reviewing construction plans under a hard hat" style="margin:12px 0 0 2px;width:183px;height:110px;background:linear-gradient(160deg,#e3b52a 0 25%,#c9ccd0 45%,#e7e8e8);position:relative">
    <svg style="position:absolute;left:74px;top:37px" width="36" height="36"><circle cx="18" cy="18" r="18" fill="#111"/><path d="M14 11L25 18L14 25Z" fill="#fff"/></svg>
    <div style="position:absolute;left:0;bottom:0;width:100%;height:13px;background:#1b1b1b"></div>
    <div style="position:absolute;left:0;bottom:13px;width:60%;height:2px;background:#c0392b"></div>
  </div>
</section>

<svg class="abs chev" style="left:140px;top:871px" viewBox="0 0 14 8"><path d="M2 1L7 6L12 1" stroke="#111" stroke-width="2" fill="none"/></svg>
<svg class="abs chev" style="left:351px;top:871px" viewBox="0 0 14 8"><path d="M2 1L7 6L12 1" stroke="#111" stroke-width="2" fill="none"/></svg>
<svg class="abs chev" style="left:562px;top:871px" viewBox="0 0 14 8"><path d="M2 1L7 6L12 1" stroke="#111" stroke-width="2" fill="none"/></svg>
<div class="abs btn-navy" style="left:112px;top:885px;width:67px">Submit</div>
<div class="abs btn-navy" style="left:325px;top:885px;width:67px">View More</div>
<div class="abs btn-navy" style="left:535px;top:885px;width:67px">View More</div>

<section class="abs" style="left:60px;top:934px;width:184px;height:166px">
  <div class="panel panel-title">latest work</div>
  <div class="work-item"><div class="pic" role="img" aria-label="Dump truck on site" style="background:linear-gradient(#6d8fb5,#d2a53a 55%,#8c8c8c)"></div><div><b>Lorem Ipsum</b><p>Lorem Ipsum is simply dummy text of the printing and typesetting</p></div></div>
  <div class="work-item"><div class="pic" role="img" aria-label="Industrial site with blue pipes" style="background:linear-gradient(#8fb6d9,#c9b89a 55%,#2c8fc9)"></div><div><b>Lorem Ipsum</b><p>Lorem Ipsum is simply dummy text of the printing and typesetting</p></div></div>
</section>

<section class="abs" style="left:289px;top:934px;width:164px;height:166px">
  <div class="panel panel-title">Our Team</div>
  <div style="display:grid;grid-template-columns:67px 67px;gap:4px 12px;margin:6px 0 0 2px">
    <div class="team-pic" role="img" aria-label="Portrait of a team member in a light shirt" style="background:linear-gradient(#f3f4f6 0%,#dfe3e8 55%,#9aa8b8 100%)"></div>
    <div class="team-pic" role="img" aria-label="Portrait of a team member in a dark suit" style="background:linear-gradient(#f6f6f6 0%,#e7e4e0 50%,#2c2f36 80%)"></div>
    <div class="team-pic" role="img" aria-label="Portrait of a team member in a dark suit" style="background:linear-gradient(#f6f6f6 0%,#ece6de 50%,#23262c 82%)"></div>
    <div class="team-pic" role="img" aria-label="Portrait of a team member in a dark suit" style="background:linear-gradient(#eef1f4 0%,#dcd7d0 50%,#2a3140 80%)"></div>
  </div>
</section>

<section class="abs news" style="left:495px;top:934px;width:184px;height:166px">
  <div class="panel panel-title">News Events</div>
  <div style="padding:11px 6px 0 4px">
    <p>Harlan Reed Kestrel Valley <em>Blanc –</em><br><em>posted on March 13, 2013 20:15</em></p>
    <p style="margin-top:6px">Media release; summer has never tasted better than with Harlan Reed's 2012 Kestrel Blanc</p>
    <p class="more">Read More</p>
    <div style="height:1px;background:#e2e2e2;margin:4px 0 12px"></div>
    <p>Harlan Reed Kestrel Valley <em>Blanc –</em><br><em>posted on March 13, 2013 20:15</em></p>
    <p class="more" style="margin-top:12px">Read More</p>
  </div>
</section>

<div class="abs social">
  <div class="s"><div><small>Share on</small><b>CIRCLENET</b></div></div>
  <div class="s"><span class="ico" style="background:#e0401c"></span><div><small>Like us on</small><b>FRIENDBOOK</b></div></div>
  <div class="s"><span class="ico" style="background:#2fa7df;border-radius:50%"></span><div><small>Follow us on</small><b style="color:#aaa">CHIRPER</b></div></div>
  <div class="s"><span class="ico" style="background:#f08a24"></span><div><small>View us on</small><b>RSS FEED</b></div></div>
  <div class="s"><span class="ico" style="background:#d9251c"></span><div><small>Watch our videos on</small><b>REELHUB</b></div></div>
</div>

<footer class="abs footer">Copyright © 2013 Verlani Construction. All rights reserved.</footer>
</body>
</html>
```